Criação de Papelaria Profissional para Roupas, Jóias & acessórios
A empresa queria:
" Locamos roupas para madrinhas , formandas e convidados de gala "

```html
<!DOCTYPE html>
<html lang="pt-BR">
<head>
<meta charset="UTF-8">
<title>Ateliê Luzia Gala — Pasta</title>
<link href="https://fonts.googleapis.com/css2?family=Cinzel:wght@500&family=Montserrat:wght@400&display=swap" rel="stylesheet">
<style>
  :root {
    --canvas: #e4e5e7;
    --folder-black: #0b0b0c;
    --folder-lift: #1a1a1c;
    --bronze: #c79a7a;
    --bronze-light: #e2bfa6;
    --text-soft: #bdb6b2;
    --photo-skin: #c9a08a;
    --photo-lip: #7a2a3a;
  }
  * { margin: 0; padding: 0; box-sizing: border-box; }
  html, body { width: 1200px; height: 1200px; overflow: hidden; }
  body {
    background: var(--canvas);
    display: flex; align-items: center; justify-content: center;
    font-family: "Montserrat", sans-serif;
  }
  .folder-spread {
    display: flex;
    width: 1040px; height: 720px;
    box-shadow: 0 18px 40px rgba(0,0,0,0.25);
  }
  .folder-panel {
    position: relative;
    width: 520px; height: 720px;
    background: linear-gradient(160deg, var(--folder-lift) 0%, var(--folder-black) 55%, var(--folder-black) 100%);
    overflow: hidden;
  }
  .folder-panel + .folder-panel { border-left: 1px solid #222; }
  .panel-texture {
    position: absolute; inset: 0;
    background: radial-gradient(ellipse at 40% 30%, rgba(255,255,255,0.05), transparent 70%);
  }
  .brand-name {
    font-family: "Cinzel", serif;
    font-weight: 500;
    color: var(--bronze);
    letter-spacing: 2px;
    text-align: center;
    line-height: 1.1;
  }
  .brand-mark {
    width: 14px; height: 14px; border-radius: 50%;
    background: var(--bronze);
    margin: 0 auto 8px;
  }
  /* back cover */
  .back-curve { position: absolute; left: 0; top: 430px; width: 520px; height: 90px; }
  .back-brand { position: absolute; left: 0; right: 0; top: 560px; }
  .back-brand .brand-name { font-size: 24px; }
  .contact-block {
    position: absolute; left: 60px; right: 30px; top: 640px;
    color: var(--text-soft); font-size: 10px; letter-spacing: 0.3px;
  }
  .contact-line { display: flex; align-items: center; gap: 6px; margin-bottom: 6px; }
  .contact-line svg { width: 10px; height: 10px; fill: var(--bronze-light); flex: none; }
  .contact-sep { margin: 0 6px; color: var(--bronze); }
  /* front cover */
  .front-band {
    position: absolute; left: 0; right: 0; top: 120px; height: 150px;
    border-top: 2px solid var(--bronze);
    border-bottom: 2px solid var(--bronze);
    background: var(--folder-black);
    display: flex;
  }
  .front-brand { width: 190px; display: flex; flex-direction: column; justify-content: center; }
  .front-brand .brand-name { font-size: 22px; }
  .hero-photo {
    flex: 1;
    background: linear-gradient(100deg, #2a1d19 0%, var(--photo-skin) 35%, var(--photo-lip) 60%, var(--photo-skin) 80%, #e6cbb8 100%);
  }
</style>
</head>
<body>
  <main class="folder-spread">
    <section class="folder-panel folder-back">
      <div class="panel-texture" role="img" aria-label="Padrão sutil de losangos escuros sobre fundo preto"></div>
      <svg class="back-curve" viewBox="0 0 520 90" preserveAspectRatio="none" aria-hidden="true">
        <defs>
          <linearGradient id="bronzeLine" x1="0" x2="1">
            <stop offset="0" stop-color="#7a5a47"/>
            <stop offset="0.5" stop-color="#e2bfa6"/>
            <stop offset="1" stop-color="#a87c62"/>
          </linearGradient>
        </defs>
        <path d="M0 80 Q260 10 520 5" fill="none" stroke="url(#bronzeLine)" stroke-width="3"/>
      </svg>
      <div class="back-brand">
        <div class="brand-mark"></div>
        <p class="brand-name">Ateliê<br>Luzia Gala</p>
      </div>
      <address class="contact-block" style="font-style:normal">
        <p class="contact-line">
          <svg viewBox="0 0 24 24"><path d="M6.6 10.8a15 15 0 0 0 6.6 6.6l2.2-2.2a1 1 0 0 1 1-.25 11 11 0 0 0 3.6.6 1 1 0 0 1 1 1V20a1 1 0 0 1-1 1A17 17 0 0 1 3 4a1 1 0 0 1 1-1h3.5a1 1 0 0 1 1 1c0 1.25.2 2.45.6 3.6a1 1 0 0 1-.25 1z"/></svg>
          +55 11 93456-7820<span class="contact-sep">|</span>
          <svg viewBox="0 0 24 24"><path d="M6.6 10.8a15 15 0 0 0 6.6 6.6l2.2-2.2a1 1 0 0 1 1-.25 11 11 0 0 0 3.6.6 1 1 0 0 1 1 1V20a1 1 0 0 1-1 1A17 17 0 0 1 3 4a1 1 0 0 1 1-1h3.5a1 1 0 0 1 1 1c0 1.25.2 2.45.6 3.6a1 1 0 0 1-.25 1z"/></svg>
          +55 11 93456-7821
        </p>
        <p class="contact-line">
          <svg viewBox="0 0 24 24"><path d="M12 2a7 7 0 0 0-7 7c0 5 7 13 7 13s7-8 7-13a7 7 0 0 0-7-7zm0 9.5A2.5 2.5 0 1 1 12 6.5a2.5 2.5 0 0 1 0 5z"/></svg>
          Rua das Sedas, 120 | Jardins | São Paulo - SP
        </p>
      </address>
    </section>
    <section class="folder-panel folder-front">
      <div class="panel-texture" role="img" aria-label="Padrão sutil de losangos escuros sobre fundo preto"></div>
      <div class="front-band">
        <div class="front-brand">
          <div class="brand-mark"></div>
          <p class="brand-name">Ateliê<br>Luzia Gala</p>
        </div>
        <div class="hero-photo" role="img" aria-label="Foto em close de modelo com batom vinho, recortada em losangos com filetes bronze"></div>
      </div>
    </section>
  </main>
</body>
</html>
```